Business Card Design for Kidvale (Hires out childrens play areas)

Looking to have a business card designed for a company we just bought. The company rents out childrens play areas.

I have uploaded a couple of examples of the kind of business card style I like. Here are two more examples:

https://quorvastudio.nz/project/bright-romp-branding/
https://imgvaultcdn.com/design_img/8841052/302917/302917_5518203_8841052_b73e19a2_image.jpg

I think a white card will be best due to all the colours in the logo.

Size we require: 3.75" x 2.25" (horizontally orientated) with a 0.125" bleed

Uploaded is two versions of our logo.

Details for the card:
1. My name: Liam Verster
2. Title: Managing Director
3. Phone no: 021 563 417
4. Email: liam@kidvale.co.nz
5. URL: www.kidvale.co.nz
6. Address:
PO Box 318625
Fernlea, Auckland

Let me know if you need anything else.

Target Market(s)

Hospitals, doctors surgeries, bed shops, etc.

Contact Information for Business Card

Details for the card:
1. My name: Liam Verster
3. Phone no: 021 563 417
5. URL: www.kidvale.co.nz
6. Address:
PO Box 318625
Fernlea, Auckland

Requirements
Should not have
• Not too busy.

```html
<!DOCTYPE html>
<html lang="en">
<head>
<meta charset="utf-8">
<title>Kidvale business card</title>
<link href="https://fonts.googleapis.com/css2?family=Roboto+Condensed:wght@400;700&family=Open+Sans:wght@400&display=swap" rel="stylesheet">
<style>
  :root{
    --stage:#e8e6e3;
    --paper:#f7f7f7;
    --green:#3fb44a;
    --purple:#6a2c9c;
    --magenta:#d4189a;
    --blue:#27479c;
    --orange:#f0571f;
    --ink-blue:#2a5fb0;
    --ink-purple:#8a2fa8;
    --ink-grey:#555a60;
    --rule:#cfcfcf;
  }
  *{box-sizing:border-box;margin:0;padding:0}
  html,body{width:1200px;height:911px;overflow:hidden;background:var(--stage)}
  .stage{position:relative;width:1200px;height:911px}
  .card{position:absolute;left:300px;width:600px;height:360px;background:var(--paper);
        box-shadow:0 2px 10px rgba(0,0,0,.12)}
  .card--front{top:70px}
  .card--back{top:481px}

  .frame-edge{position:absolute;display:flex;gap:3px}
  .frame-edge span{flex:1}
  .frame-edge--top{top:0;left:0;right:0;height:9px}
  .frame-edge--bottom{bottom:0;left:0;right:0;height:9px}
  .frame-edge--left{top:0;bottom:0;left:0;width:9px;flex-direction:column}
  .frame-edge--right{top:0;bottom:0;right:0;width:9px;flex-direction:column}
  .c-green{background:var(--green)} .c-purple{background:var(--purple)}
  .c-magenta{background:var(--magenta)} .c-blue{background:var(--blue)}
  .c-orange{background:var(--orange)}

  .brand{position:absolute;left:52px;top:148px;display:flex;align-items:center;gap:12px;
         font-family:"Roboto Condensed",sans-serif;font-weight:700;font-size:46px;color:var(--ink-purple)}
  .brand-dot{width:30px;height:30px;border-radius:50%;background:var(--orange)}

  .contact{position:absolute;left:318px;top:96px;width:240px;font-family:"Open Sans",sans-serif}
  .contact-name{font-family:"Roboto Condensed",sans-serif;font-weight:700;font-size:22px;color:var(--ink-blue);letter-spacing:.3px}
  .contact-title{font-family:"Roboto Condensed",sans-serif;font-size:15px;color:var(--ink-purple);letter-spacing:.3px;margin-bottom:12px}
  .contact-rule{height:1px;background:var(--rule);margin:0 0 14px -30px;width:260px}
  .contact-address{font-size:13px;line-height:19px;color:var(--ink-grey);margin-bottom:14px}
  .contact-line{display:flex;align-items:center;gap:9px;font-size:13px;line-height:20px;color:var(--ink-grey)}
  .contact-line svg{width:11px;height:11px;fill:var(--ink-blue);flex:none}

  .back-url{position:absolute;left:40px;top:60px;writing-mode:vertical-rl;
            font-family:"Open Sans",sans-serif;font-size:12px;letter-spacing:6px;color:var(--ink-grey)}
  .back-brand{position:absolute;left:0;right:0;top:150px;display:flex;justify-content:center;align-items:center;gap:12px;
              font-family:"Roboto Condensed",sans-serif;font-weight:700;font-size:46px;color:var(--ink-purple)}
  .back-brand .brand-dot{background:var(--magenta)}
</style>
</head>
<body>
<main class="stage">

  <section class="card card--front" aria-label="Card front">
    <div class="frame-edge frame-edge--top"><span class="c-purple"></span><span class="c-green"></span><span class="c-magenta"></span><span class="c-purple"></span><span class="c-green"></span></div>
    <div class="frame-edge frame-edge--bottom"><span class="c-blue"></span><span class="c-magenta"></span><span class="c-purple"></span><span class="c-green"></span><span class="c-orange"></span></div>
    <div class="frame-edge frame-edge--left"><span class="c-green"></span><span class="c-blue"></span><span class="c-orange"></span></div>
    <div class="frame-edge frame-edge--right"><span class="c-green"></span><span class="c-purple"></span><span class="c-blue"></span></div>

    <div class="brand"><span class="brand-dot"></span>Kidvale</div>

    <div class="contact">
      <p class="contact-name">LIAM VERSTER</p>
      <p class="contact-title">MANAGING DIRECTOR</p>
      <div class="contact-rule"></div>
      <p class="contact-address">PO Box 318625<br>Fernlea, Auckland</p>
      <p class="contact-line"><svg viewBox="0 0 12 12" aria-hidden="true"><path d="M2.5 0.5l2 2-1 1.3c.6 1.6 1.9 2.9 3.5 3.6l1.3-1 2.2 2-1.4 2C5 10.2 1.8 7 .5 2z"/></svg>021 563 417</p>
      <p class="contact-line"><svg viewBox="0 0 12 12" aria-hidden="true"><path d="M0 2h12v8H0zM1 3l5 3.5L11 3v-.1H1z" fill-rule="evenodd"/></svg>liam@kidvale.co.nz</p>
      <p class="contact-line"><svg viewBox="0 0 12 12" aria-hidden="true"><circle cx="6" cy="6" r="6"/></svg>www.kidvale.co.nz</p>
    </div>
  </section>

  <section class="card card--back" aria-label="Card back">
    <div class="frame-edge frame-edge--top"><span class="c-magenta"></span><span class="c-purple"></span><span class="c-blue"></span></div>
    <div class="frame-edge frame-edge--bottom"><span class="c-green"></span><span class="c-purple"></span><span class="c-magenta"></span><span class="c-blue"></span></div>
    <div class="frame-edge frame-edge--left"><span class="c-orange"></span><span class="c-blue"></span><span class="c-purple"></span></div>
    <div class="frame-edge frame-edge--right"><span class="c-orange"></span><span class="c-blue"></span><span class="c-purple"></span><span class="c-green"></span></div>

    <p class="back-url">www.kidvale.co.nz</p>
    <div class="back-brand"><span class="brand-dot"></span>Kidvale</div>
  </section>

</main>
</body>
</html>
```